Business Card Design Project

I need a business card designed for FableHarbor, a website which has people share their fictional story ideas with others. The business cards should incorporate the websites's logo, which can be found at www.fableharbor-example.com .

Target Market(s)

These will be primarily used in business development activities, not given to customers. It therefore needs to have a clean, professional appearance, and yet communicate what the company is trying to achieve as a bold startup.

Industry/Entity Type

Business

```html
<!DOCTYPE html>
<html lang="en">
<head>
<meta charset="utf-8">
<title>FableHarbor Business Card</title>
<link rel="stylesheet" href="https://fonts.googleapis.com/css2?family=Montserrat:wght@500&family=Roboto:wght@500&family=Open+Sans:wght@400&display=swap">
<style>
  :root {
    --backdrop: #e6e7e8;
    --navy: #1f4465;
    --slate: #6b7d99;
    --mist: #cddff0;
    --ice: #e8eef5;
    --icon: #c7d6e6;
  }
  html, body {
    margin: 0;
    padding: 0;
    width: 1200px;
    height: 1000px;
    overflow: hidden;
    background: var(--backdrop);
  }
  .canvas {
    position: relative;
    width: 1200px;
    height: 1000px;
  }
  .card {
    position: absolute;
    display: block;
  }
  .card--front { left: 305px; top: 195px; }
  .card--back  { left: 338px; top: 619px; }
  .front-name {
    font-family: "Montserrat", sans-serif;
    font-weight: 500;
    font-size: 34px;
    fill: var(--ice);
  }
  .back-name {
    font-family: "Roboto", sans-serif;
    font-weight: 500;
    font-size: 24px;
    fill: var(--navy);
  }
  .web-address {
    font-family: "Open Sans", sans-serif;
    font-weight: 400;
    font-size: 16px;
    fill: var(--ice);
  }
</style>
</head>
<body>
<main class="canvas">

  <svg class="card card--front" width="535" height="305" viewBox="0 0 535 305" aria-label="Business card front">
    <defs>
      <clipPath id="front-edge"><rect width="535" height="305"/></clipPath>
    </defs>
    <rect class="card-face" width="535" height="305" fill="var(--navy)"/>
    <circle class="accent-disc" cx="462" cy="111" r="82" fill="var(--slate)" clip-path="url(#front-edge)"/>
    <circle class="brand-dot" cx="67" cy="152" r="26" fill="var(--mist)"/>
    <text class="front-name" x="107" y="164">FableHarbor</text>
  </svg>

  <svg class="card card--back" width="538" height="308" viewBox="0 0 538 308" aria-label="Business card back">
    <rect class="card-face" width="538" height="308" fill="var(--mist)"/>
    <path class="contact-panel" d="M197,0 C210,110 260,180 317,219 C272,248 240,280 217,308 L538,308 L538,0 Z" fill="var(--navy)"/>
    <text class="back-name" x="33" y="129">FableHarbor</text>

    <g class="contact-icons" fill="var(--icon)">
      <g class="icon-email" transform="translate(328,133)">
        <path d="M0,6 L9,0 L18,6 L18,17 L0,17 Z"/>
        <path d="M2,7 L9,12 L16,7" fill="none" stroke="var(--navy)" stroke-width="1.4"/>
      </g>
      <g class="icon-phone" transform="translate(331,162)">
        <path d="M3,2 C1,4 1,7 4,11 C7,15 10,16 12,15 L14,13 L11,10 L9,11 C7,10 5,8 5,6 L6,4 L3,1 Z"/>
      </g>
      <rect class="icon-social" x="331" y="192" width="20" height="20" rx="3"/>
    </g>

    <text class="web-address" x="528" y="287" text-anchor="end">www.fableharbor-example.com</text>
  </svg>

</main>
</body>
</html>
```